Property Management business needs Business cards designed

We provide a premium property management service based in Sydney's Norther Beaches. We want people to feel confident in choosing us to manage their investment properties. We offer a much more personalized service than other estate agents.
We want a modern clean design. Something that shows confidence without being complicated.
Logo attached.

Target Market(s)

35-70yo Male and Female with strong property portfolios within Sydney's Norther Beaches

Industry/Entity Type

Property Management

Contact Information for Business Card

Address: Suite 7, 12-14 Kelvin Parade, Harlow NSW 2188
Two separate named cards.
Tom Ardley - 0491 570 118 tom@harbourvaleestates.com.au
Clara Dunmore - 0491 570 263 clara@harbourvaleestates.com.au

Requirements
Must have
• Business logo, name, number, address, email.

```html
<!DOCTYPE html>
<html lang="en">
<head>
<meta charset="utf-8">
<title>Harbourvale Estates – Business Cards</title>
<link rel="stylesheet" href="https://fonts.googleapis.com/css2?family=Arimo:wght@400;700&display=swap">
<style>
  :root {
    --backdrop: #5a5a5a;
    --card-black: #000000;
    --teal: #1b8291;
    --teal-band: #177f8e;
    --white: #ffffff;
    --cream: #eeeadb;
    --band-text: #0d2a30;
  }
  * { margin: 0; padding: 0; box-sizing: border-box; }
  html, body {
    width: 1200px;
    height: 675px;
    overflow: hidden;
    background: var(--backdrop);
    font-family: "Arimo", Arial, sans-serif;
  }
  .card-set {
    position: absolute;
    left: 40px;
    top: 172px;
    display: flex;
    gap: 40px;
  }
  .business-card {
    position: relative;
    width: 540px;
    height: 330px;
    background: var(--card-black);
    overflow: hidden;
    box-shadow: 0 8px 24px rgba(0,0,0,0.35);
  }
  .brand {
    position: absolute;
    top: 56px;
    right: 38px;
    display: flex;
    align-items: center;
    gap: 9px;
  }
  .brand-dot {
    width: 14px;
    height: 14px;
    border-radius: 50%;
    background: var(--teal);
  }
  .brand-name {
    color: var(--cream);
    font-weight: 700;
    font-size: 21px;
    letter-spacing: 0.6px;
    white-space: nowrap;
  }
  .contact {
    position: absolute;
    left: 59px;
    top: 90px;
    color: var(--white);
    font-size: 15px;
    line-height: 1.2;
    white-space: nowrap;
  }
  .contact-name {
    color: var(--teal);
    font-size: 22px;
    line-height: 1.1;
  }
  .contact-role { margin-bottom: 12px; }
  .contact-lines { margin-bottom: 11px; }
  .company { color: var(--teal); }
  .web-band {
    position: absolute;
    left: 0;
    bottom: 0;
    width: 100%;
    height: 38px;
    background: var(--teal-band);
    display: flex;
    align-items: center;
    justify-content: center;
  }
  .web-address {
    color: var(--band-text);
    font-size: 15px;
  }
</style>
</head>
<body>
  <div class="card-set">
    <div class="business-card">
      <div class="brand">
        <span class="brand-dot"></span>
        <span class="brand-name">HARBOURVALE ESTATES</span>
      </div>
      <div class="contact">
        <p class="contact-name">Tom Ardley</p>
        <p class="contact-role">Director</p>
        <div class="contact-lines">
          <p>0491 570 118</p>
          <p>tom@harbourvaleestates.com.au</p>
        </div>
        <p class="company">Harbourvale Estates</p>
        <p>Suite 7, 12-14 Kelvin Parade</p>
        <p>Harlow NSW 2188</p>
      </div>
      <div class="web-band">
        <p class="web-address">www.harbourvaleestates.com.au</p>
      </div>
    </div>

    <div class="business-card">
      <div class="brand">
        <span class="brand-dot"></span>
        <span class="brand-name">HARBOURVALE ESTATES</span>
      </div>
      <div class="contact">
        <p class="contact-name">Clara Dunmore</p>
        <p class="contact-role">Director</p>
        <div class="contact-lines">
          <p>0491 570 263</p>
          <p>clara@harbourvaleestates.com.au</p>
        </div>
        <p class="company">Harbourvale Estates</p>
        <p>Suite 7, 12-14 Kelvin Parade</p>
        <p>Harlow NSW 2188</p>
      </div>
      <div class="web-band">
        <p class="web-address">www.harbourvaleestates.com.au</p>
      </div>
    </div>
  </div>
</body>
</html>
```